New Brand - Website Design (4 Pages)

We are launching a new brand for electronic cigarettes. We already have logo and packaging done and would like a web design to go with it.

We are interested in the following deliverables:

1) Home Page Design
2) Check Out Design
3) How it Works Page
4) Secondary Template Page Design

Looking for a 60s modern look and something that is consistent with our logo and packaging.

Industry/Entity Type

Electronic

Requirements
Must have
• Consistent with logo and packaging (Use Logo Attached)
White background

Example (Functionality & Design): http://www.torvex.co.uk/
Example (Design): http://www.quillharbor.com/

We want the design more like quillharbor but the functionality the same as torvex.

Top Bar: Pebble Arcs Kits; Cartridge Refills; How it Works; Contact; My Account; Checkout
Should not have
• Stock List or Search Bar or Newsletter Signup

```html
<!DOCTYPE html>
<html lang="en">
<head>
<meta charset="utf-8">
<title>Pebble Arcs — Home</title>
<link rel="stylesheet" href="https://fonts.googleapis.com/css2?family=Open+Sans:wght@400;600&family=Noto+Serif:wght@400&display=swap">
<style>
  :root {
    --page-bg: #eceef2;
    --panel-bg: #ffffff;
    --nav-bg: #8ed8f2;
    --nav-divider: #79c4df;
    --nav-text: #2b4a5a;
    --accent: #1a8fb5;
    --accent-bright: #19b4e6;
    --heading-text: #3a3a3a;
    --body-text: #555b60;
    --rule: #c9ccd0;
    --hero-dark: #262626;
    --hero-mid: #444444;
    --price: #8fd5f2;
    --button-top: #f4e34a;
    --button-bottom: #f9b232;
    --social: #5a7fb0;
    --ink: #111111;
  }
  * { box-sizing: border-box; margin: 0; padding: 0; }
  html, body { width: 1124px; height: 1200px; overflow: hidden; }
  body {
    background: var(--page-bg);
    font-family: "Open Sans", Arial, sans-serif;
    color: var(--body-text);
    position: relative;
  }
  .site { position: absolute; left: 132px; top: 0; width: 860px; }

  /* Header */
  .site-header { height: 112px; position: relative; }
  .brand {
    position: absolute; left: 0; top: 22px;
    display: flex; align-items: center; gap: 12px;
  }
  .brand-dot { width: 60px; height: 60px; border-radius: 50%; background: var(--nav-bg); }
  .brand-name { font-size: 32px; font-weight: 600; color: var(--ink); letter-spacing: 0.5px; }
  .bag-box {
    position: absolute; right: 0; top: 17px; width: 227px;
    background: var(--panel-bg); border: 1px solid #dcdfe3;
    font-size: 12.5px; color: #333;
  }
  .bag-box .bag { height: 39px; display: flex; align-items: center; gap: 6px; padding-left: 12px; border-bottom: 1px solid #dcdfe3; }
  .bag-box .help { height: 32px; display: flex; align-items: center; padding-left: 19px; }

  /* Navigation */
  .main-nav { display: flex; height: 44px; background: var(--nav-bg); }
  .main-nav a {
    display: flex; align-items: center; padding: 0 17.5px;
    font-size: 13px; color: var(--nav-text); text-decoration: none;
    border-right: 1px solid var(--nav-divider);
  }
  .main-nav a:last-child { border-right: none; }

  /* Offers */
  .offer-bar {
    height: 62px; background: var(--panel-bg);
    display: flex; align-items: center;
  }
  .offer { display: flex; align-items: center; gap: 10px; }
  .offer-shipping { padding-left: 9px; width: 296px; height: 38px; border-right: 1px solid #e2e4e7; }
  .offer-gift { padding-left: 34px; }
  .offer-title { font-size: 17.5px; color: var(--accent); }
  .offer-note { font-size: 11px; color: #444; margin-left: 6px; }

  /* Hero */
  .hero {
    position: relative; height: 334px; overflow: hidden;
    background: radial-gradient(ellipse at 30% 40%, var(--hero-mid), var(--hero-dark) 75%);
  }
  .hero-visual {
    position: absolute; left: 352px; top: 0; width: 508px; height: 334px;
    background: linear-gradient(100deg, rgba(40,40,40,0) 0%, #3f6b2c 45%, #6aa53a 70%, #7a7a7a 100%);
  }
  .hero-copy { position: absolute; left: 48px; top: 72px; width: 260px; text-align: center; }
  .hero-title { font-family: "Noto Serif", Georgia, serif; font-size: 34px; font-weight: 400; color: #f2f2f2; white-space: nowrap; margin-left: -12px; text-align: left; }
  .hero-price { font-size: 36px; color: var(--price); margin-top: 30px; }
  .shop-now {
    display: flex; align-items: center; justify-content: center;
    width: 98px; height: 98px; border-radius: 50%; margin: 12px auto 0;
    background: linear-gradient(var(--button-top), var(--button-bottom));
    font-family: "Noto Serif", Georgia, serif; font-size: 17px; color: #3a3420; text-decoration: none;
  }
  .hero-arrow { position: absolute; top: 152px; }
  .hero-arrow.prev { left: 9px; }
  .hero-arrow.next { right: 9px; }

  /* Flavours */
  .flavours { background: var(--panel-bg); height: 238px; padding-top: 18px; }
  .section-rule { display: flex; align-items: center; gap: 10px; padding: 0 10px; }
  .section-rule::before, .section-rule::after { content: ""; flex: 1; border-top: 1px dotted #999; }
  .section-rule h2 { font-size: 17.5px; font-weight: 400; color: var(--heading-text); }
  .flavour-list { display: flex; justify-content: space-between; padding: 12px 10px 0; list-style: none; }
  .flavour { width: 128px; text-align: center; }
  .flavour-badge {
    width: 126px; height: 126px; border-radius: 50%; background: var(--accent-bright);
    display: flex; align-items: center; justify-content: center;
  }
  .flavour-photo { width: 86px; height: 86px; border-radius: 50%; }
  .flavour-name { margin-top: 12px; font-size: 16px; color: #4a4a4a; }

  /* Info columns */
  .info { display: flex; background: var(--panel-bg); margin-top: 18px; height: 309px; }
  .info-col { padding: 14px 18px 0; border-right: 1px solid #e6e8eb; }
  .info-col:last-child { border-right: none; }
  .col-about { width: 290px; }
  .col-steps { width: 281px; }
  .col-features { width: 289px; }
  .info-col h3 {
    font-size: 14px; font-weight: 400; color: var(--accent);
    padding-bottom: 2px; border-bottom: 1px solid #dde0e3; margin-bottom: 14px;
  }
  .info-col p { font-size: 11px; line-height: 17.5px; margin-left: 2px; }
  .info-col p + p { margin-top: 19px; }
  .read-more { display: inline-block; margin-top: 9px; margin-left: 2px; font-size: 11px; color: var(--accent); text-decoration: none; }
  .steps { list-style: none; }
  .step { display: flex; align-items: center; gap: 12px; height: 58px; }
  .step-num {
    flex: none; width: 32px; height: 32px; border-radius: 50%;
    background: var(--accent-bright); color: #fff; font-size: 15px;
    display: flex; align-items: center; justify-content: center; margin-left: 6px;
  }
  .step p { font-size: 11px; line-height: 16px; margin: 0; }
  .product-shot {
    width: 140px; height: 100px; margin: 22px 0 0 60px;
    background: linear-gradient(#f2f2f2 0 18%, #1d1b1c 18%);
  }

  /* Footer */
  .site-footer { text-align: center; margin-top: 16px; }
  .social { display: flex; justify-content: center; gap: 8px; list-style: none; }
  .social li { width: 26px; height: 26px; border-radius: 50%; background: var(--social); }
  .copyright { margin-top: 9px; font-size: 11px; color: #444; }
</style>
</head>
<body>
  <div class="site">
    <header class="site-header">
      <div class="brand">
        <span class="brand-dot"></span>
        <span class="brand-name">Pebble Arcs</span>
      </div>
      <div class="bag-box">
        <div class="bag">
          <svg width="22" height="20" viewBox="0 0 22 20" aria-hidden="true">
            <path d="M1 2h4l3 11h10l2-8H7" fill="none" stroke="#222" stroke-width="1.6"/>
            <circle cx="9" cy="17" r="1.6" fill="#222"/><circle cx="17" cy="17" r="1.6" fill="#222"/>
          </svg>
          <span>( 0 ) Items in your Bag</span>
        </div>
        <div class="help">Call us for Help : +44 20 7946 0318</div>
      </div>
    </header>

    <nav class="main-nav">
      <a href="#">Pebble Arcs Kits</a>
      <a href="#">Cartridge Refills</a>
      <a href="#">How it Works</a>
      <a href="#">Contact</a>
      <a href="#">My Account</a>
      <a href="#">Checkout</a>
    </nav>

    <div class="offer-bar">
      <div class="offer offer-shipping">
        <svg width="32" height="20" viewBox="0 0 32 20" aria-hidden="true">
          <rect x="1" y="3" width="19" height="12" fill="#e6e6e6" stroke="#666"/>
          <path d="M20 7h6l4 4v4H20z" fill="#cfcfcf" stroke="#666"/>
          <circle cx="7" cy="17" r="2.2" fill="#444"/><circle cx="25" cy="17" r="2.2" fill="#444"/>
        </svg>
        <span class="offer-title">FREE Shipping</span>
        <span class="offer-note">Order over £29.50</span>
      </div>
      <div class="offer offer-gift">
        <svg width="22" height="24" viewBox="0 0 22 24" aria-hidden="true">
          <rect x="2" y="9" width="18" height="14" fill="#e24b2b"/>
          <rect x="1" y="6" width="20" height="4" fill="#f06a3a"/>
          <rect x="9.5" y="6" width="3" height="17" fill="#f7c531"/>
          <path d="M11 6C8 1 4 2 6 6M11 6c3-5 7-4 5 0" fill="none" stroke="#f7c531" stroke-width="1.6"/>
        </svg>
        <span class="offer-title">Order over £29.50 and Get Gift</span>
      </div>
    </div>

    <section class="hero">
      <div class="hero-visual" role="img" aria-label="Apple flavoured cartridge pack resting in a wooden bucket of green apples"></div>
      <div class="hero-copy">
        <h1 class="hero-title">Apple Flavoured</h1>
        <div class="hero-price">£29.50</div>
        <a class="shop-now" href="#">Shop Now</a>
      </div>
      <svg class="hero-arrow prev" width="20" height="34" viewBox="0 0 20 34" aria-label="Previous slide">
        <path d="M18 1L2 17l16 16" fill="none" stroke="#fff" stroke-width="1.6"/>
      </svg>
      <svg class="hero-arrow next" width="20" height="34" viewBox="0 0 20 34" aria-label="Next slide">
        <path d="M2 1l16 16L2 33" fill="none" stroke="#fff" stroke-width="1.6"/>
      </svg>
    </section>

    <section class="flavours">
      <div class="section-rule"><h2>Flavours</h2></div>
      <ul class="flavour-list">
        <li class="flavour"><div class="flavour-badge"><div class="flavour-photo" role="img" aria-label="Red apple" style="background: radial-gradient(circle at 40% 35%, #e23a36, #8e0f14);"></div></div><div class="flavour-name">Apple</div></li>
        <li class="flavour"><div class="flavour-badge"><div class="flavour-photo" role="img" aria-label="Cherries" style="background: radial-gradient(circle at 50% 60%, #b8141c, #19b4e6 72%);"></div></div><div class="flavour-name">Crown Berry</div></li>
        <li class="flavour"><div class="flavour-badge"><div class="flavour-photo" role="img" aria-label="Cinnamon sticks" style="background: radial-gradient(circle, #a5532a, #19b4e6 72%);"></div></div><div class="flavour-name">Chinnamon</div></li>
        <li class="flavour"><div class="flavour-badge"><div class="flavour-photo" role="img" aria-label="Mint leaves" style="background: radial-gradient(circle, #3c8c3a, #19b4e6 72%);"></div></div><div class="flavour-name">Menthol</div></li>
        <li class="flavour"><div class="flavour-badge"><div class="flavour-photo" role="img" aria-label="Loose tobacco leaf" style="background: radial-gradient(circle, #8a7554, #4a3c28);"></div></div><div class="flavour-name">Crown Tobacco</div></li>
      </ul>
    </section>

    <section class="info">
      <div class="info-col col-about">
        <h3>Pebble Arcs</h3>
        <p>Lorem ipsum dolor sit amet, consectetur adipiscing elit. Curabitur euismod, mauris vitae sodales consequat, orci lectus imperdiet ligula, vitae varius lacus risus sed arcu. Proin diam magna, adipiscing vel lectus vel, laoreet elementum velit. Sed sodales urnaporttitor urna.</p>
        <p>Lorem ipsum dolor sit amet, consectetur adipiscing elit. Curabitur euismod, mauris vitae sodales consequat, orci lectus imperdiet ligula</p>
        <a class="read-more" href="#">Read more...</a>
      </div>
      <div class="info-col col-steps">
        <h3>How it Works</h3>
        <ol class="steps">
          <li class="step"><span class="step-num">1</span><p>Proin diam magna, adipiscing vel lectus vel, laoreet elementu</p></li>
          <li class="step"><span class="step-num">2</span><p>Proin diam magna, adipiscing vel lectus vel, laoreet elementu</p></li>
          <li class="step"><span class="step-num">3</span><p>Proin diam magna, adipiscing vel lectus vel, laoreet elementu</p></li>
          <li class="step"><span class="step-num">4</span><p>Proin diam magna, adipiscing vel lectus vel, laoreet elementu</p></li>
        </ol>
      </div>
      <div class="info-col col-features">
        <h3>Features of Pebble Arcs</h3>
        <p>Lorem ipsum dolor sit amet, consectetur adipiscing elit. Curabitur euismod, mauris vitae sodales consequat, orci lectus imperdiet ligula, vitae varius lacus risus sed arcu. Proin diam magna, adipiscing vel lectus vel, laoreet elementum velit. Sed sodales urnaporttitor urna.</p>
        <div class="product-shot" role="img" aria-label="Black product pack"></div>
      </div>
    </section>

    <footer class="site-footer">
      <ul class="social">
        <li aria-label="Social link"></li>
        <li aria-label="Social link"></li>
        <li aria-label="Social link"></li>
      </ul>
      <p class="copyright">Copyright © 2013 Pebble Arcs, LLC All rights reserved.</p>
    </footer>
  </div>
</body>
</html>
```